A church planting organization designed specifically for the urban centers

I am looking to create a 5 page website.

i would like to create an (1) Homepage, (2) About Us, (3) Donate, (4) Contact Us, and (5) Partner Page

The name of the organization is called Harborline Faith Builders which is an organization designed to help establish churches in a central city context.

I would like the colors to incorporate the colors of the logo which is a black, white, and orange. I would be okay with adding a
green for an accent. I love the use of orange filters when appropriate.

We would like to have a design that pops at first glance. I have included some graphs that can be recreated or recolored to better fit with one's design.

Primary Goal:
A marketing tool to attract (1) Harborline Faith Builders who desire to plant and; (2) donors; (3) churches or church plant networks that have an interest in partnering financially or through collective impact. Information should be provided on how to become part of the movement.

Secondary Goal:
Make the argument why central city church plants are needed
Make the argument why Multi-Ethnic churches are needed
Candidates can apply for residency at one of the network churches
Churches can apply to join the network
Church Planting Networks can apply to partner

Target Market(s)

Target Market
Church Planting Networks
Ethnic Homogenous Churches
Church Networks
Church Planters
Diversity Seekers
Impactors of Distressed Communities

Coding

Coded - Design and coding required

Number of Pages Required

5+ page

Font styles to use
Other font styles liked:
• I have uploaded our font

Requirements
Must have
• Pages that pop at first glance
Nice to have
• I would like the graphs I attached recreated or recolored to match your design layout

```html
<!DOCTYPE html>
<html lang="en">
<head>
<meta charset="utf-8">
<title>Harborline Faith Builders</title>
<link rel="stylesheet" href="https://fonts.googleapis.com/css2?family=Montserrat:wght@700;800&family=Nunito:wght@400;600;700&display=swap">
<style>
:root{
  --orange:#fa6f0c;
  --green:#3aab11;
  --ink:#2b2b2b;
  --black:#1f1f1f;
  --grey:#ececec;
  --line:#dcdcdc;
  --white:#fff;
}
*{box-sizing:border-box;margin:0;padding:0}
html,body{width:1200px;height:2941px;overflow:hidden}
body{font-family:"Nunito",sans-serif;color:var(--ink);background:var(--white);position:relative}
.heading{font-family:"Montserrat",sans-serif;font-weight:800;text-transform:uppercase}
.site-header{height:108px;display:flex;align-items:center;justify-content:space-between;padding:0 73px 0 74px}
.brand{font-family:"Montserrat",sans-serif;font-weight:800;font-size:30px;line-height:34px;color:var(--ink);text-transform:uppercase;letter-spacing:.3px}
.main-nav{display:flex;gap:48px;font-family:"Montserrat",sans-serif;font-weight:800;font-size:14.5px;text-transform:uppercase}
.main-nav a{color:var(--ink);text-decoration:none}
.main-nav a.active{color:var(--green)}
.hero{position:relative;height:707px;background:linear-gradient(100deg,#0c0b0a 0%,#2a2418 35%,#6c7d3a 55%,#3a2f22 75%,#14100c 100%)}
.hero-copy{position:absolute;left:74px;top:296px;color:var(--white)}
.hero-copy h1{font-size:36px;line-height:48px;letter-spacing:.5px}
.hero-copy p{font-size:20.5px;line-height:30px;font-weight:600;margin-top:10px;width:540px}
.btn{display:inline-block;background:var(--green);color:var(--white);font-family:"Montserrat",sans-serif;font-weight:700;font-size:17.5px;text-transform:uppercase;text-decoration:none;width:172px;height:52px;line-height:52px;text-align:center;letter-spacing:.4px}
.hero .btn{margin-top:38px}
.mission{position:absolute;left:74px;top:704px;width:1052px;height:224px;border:7px solid var(--line);background:var(--orange);color:var(--white);text-align:center;padding-top:44px}
.mission h2{font-size:32px;letter-spacing:.3px}
.mission p{font-size:25.5px;line-height:38px;font-weight:600;margin-top:8px;padding:0 30px}
.problem{position:absolute;top:1001px;left:0;width:1200px;height:607px;display:flex}
.problem-text{width:615px;background:var(--grey);padding:68px 0 0 74px}
.problem-text h2{font-size:32px;color:var(--ink)}
.problem-text p{font-size:16.5px;line-height:33.2px;font-weight:600;width:475px;margin-top:17px}
.problem-text .btn{margin-top:26px}
.problem-photo{flex:1;background:linear-gradient(180deg,#1b6fd8 0%,#5f9be0 45%,#d9e6f3 80%,#8aa070 100%)}
.barriers{position:absolute;top:1660px;left:0;width:1200px;text-align:center}
.barriers h2{font-size:31px}
.barrier{position:absolute;width:260px;text-align:center}
.barrier .ring{width:99px;height:99px;border:3px solid var(--orange);border-radius:50%;margin:0 auto;display:flex;align-items:center;justify-content:center;background:var(--white)}
.barrier .label{font-size:18.5px;line-height:29px;font-weight:600;margin-top:11px;letter-spacing:.3px}
.faq{position:absolute;top:2264px;left:0;width:1200px;height:481px;background:var(--grey)}
.faq h2{text-align:center;font-size:31px;margin-top:50px}
.faq-col{position:absolute;top:138px;width:512px;display:flex;flex-direction:column;gap:11px}
.faq-col.left{left:74px}
.faq-col.right{left:617px}
.faq-item{display:flex;background:var(--white);min-height:53px}
.faq-letter{width:50px;background:var(--black);color:var(--white);font-family:"Montserrat",sans-serif;font-weight:800;font-size:21px;display:flex;align-items:center;justify-content:center;flex-shrink:0}
.faq-q{flex:1;display:flex;align-items:center;justify-content:space-between;padding:0 28px 0 21px;font-size:18px;line-height:25px}
.faq-q svg{flex-shrink:0;margin-left:12px}
.faq-item.open .faq-q{display:block;padding:16px 28px 12px 21px;position:relative}
.faq-item.open .faq-title{color:var(--orange);font-weight:600;font-size:18.5px;line-height:25px;width:390px}
.faq-item.open .faq-answer{font-size:14px;line-height:21px;margin-top:6px;width:400px}
.faq-item.open svg{position:absolute;right:20px;top:22px}
.site-footer{position:absolute;top:2790px;left:0;width:1200px;text-align:center}
.foot-nav{display:flex;justify-content:center;gap:48px;font-family:"Montserrat",sans-serif;font-weight:800;font-size:14.5px;text-transform:uppercase}
.foot-nav a{color:var(--ink);text-decoration:none}
.copyright{font-size:14.5px;margin-top:18px}
.social{display:flex;justify-content:center;gap:22px;margin-top:20px}
.social span{width:20px;height:20px;border-radius:50%;background:var(--orange)}
</style>
</head>
<body>
<header class="site-header">
  <div class="brand">Harborline Faith<br>Builders</div>
  <nav class="main-nav">
    <a class="active" href="#">Home</a><a href="#">About Us</a><a href="#">Donate</a><a href="#">Contact Us</a><a href="#">Partners</a>
  </nav>
</header>

<section class="hero" role="img" aria-label="Pastor speaking on a stage before a lit screen, with a cross of light to the left">
  <div class="hero-copy">
    <h1 class="heading">Welcome to<br>Harborline Faith<br>Builders</h1>
    <p>We are an organization designed to help establish churches in a central city context.</p>
    <a class="btn" href="#">Donate Now</a>
  </div>
</section>

<div class="mission">
  <h2 class="heading">Mission Statement</h2>
  <p>“To multiply the gospel in urban centers by raising up and equipping church planters in a central city or multi-ethnic context.”</p>
</div>

<section class="problem">
  <div class="problem-text">
    <h2 class="heading">Problem</h2>
    <p>Problem-The church planting scene in the central city of Milwaukee is fairly problematic. While church planting networks have been planting many churches in a suburban context each year, the central city has been ignored. Unfortunately, many church planting organizations have little to no understanding of the central city context and have therefore avoided planting central city churches in Milwaukee and beyond. To exacerbate the issue, Black churches historically do not plant churches.</p>
    <a class="btn" href="#">Read More</a>
  </div>
  <div class="problem-photo" role="img" aria-label="White country church with a steeple and cross under a blue sky"></div>
</section>

<section class="barriers">
  <h2 class="heading">Barrier to Address</h2>
  <div class="barrier" style="left:110px;top:92px">
    <div class="ring"><svg width="46" height="46" viewBox="0 0 46 46" fill="var(--black)"><circle cx="14" cy="8" r="5"/><path d="M10 15h9l3 12-4 16h-5l3-14-4-4-5 18H2l6-20z"/><rect x="24" y="16" width="16" height="14" rx="2"/></svg></div>
    <div class="label">Suburban Support<br>Raising Model</div>
  </div>
  <div class="barrier" style="left:469px;top:92px">
    <div class="ring"><svg width="48" height="30" viewBox="0 0 48 30" fill="var(--black)"><circle cx="24" cy="7" r="6"/><circle cx="10" cy="10" r="5"/><circle cx="38" cy="10" r="5"/><path d="M13 28c0-8 5-12 11-12s11 4 11 12z"/><path d="M1 28c0-6 4-9 9-9 2 0 3 .5 4 1-2 2-3 5-3 8z"/><path d="M47 28c0-6-4-9-9-9-2 0-3 .5-4 1 2 2 3 5 3 8z"/></svg></div>
    <div class="label">Launch<br>Team</div>
  </div>
  <div class="barrier" style="left:831px;top:92px">
    <div class="ring"><svg width="44" height="44" viewBox="0 0 44 44" fill="var(--black)"><rect x="21" y="2" width="2" height="10"/><rect x="17" y="5" width="10" height="2"/><path d="M22 12L4 28h5v14h10v-9h6v9h10V28h5z"/></svg></div>
    <div class="label">Church Planter<br>Assessment</div>
  </div>
  <div class="barrier" style="left:290px;top:311px">
    <div class="ring"><svg width="52" height="36" viewBox="0 0 52 36" fill="var(--black)"><path d="M2 8l10-4 8 4 6-3 6 3 8-4 10 4-4 12-8 10c-2 2-5 2-7 0l-4-3-4 3c-2 1-4 1-5 0L6 20z"/></svg></div>
    <div class="label">Cultural<br>Competency</div>
  </div>
  <div class="barrier" style="left:652px;top:311px">
    <div class="ring"><svg width="44" height="38" viewBox="0 0 44 38" fill="var(--black)"><ellipse cx="18" cy="14" rx="16" ry="11"/><path d="M6 22l-3 8 9-5z"/><path d="M36 12c5 2 7 6 6 10-1 3-3 5-6 6l3 7-9-5c-5 0-9-2-11-5 9 0 16-5 17-13z"/></svg></div>
    <div class="label">Cultural Communication<br>Priority</div>
  </div>
</section>

<section class="faq">
  <h2 class="heading">FAQ</h2>
  <div class="faq-col left">
    <div class="faq-item"><div class="faq-letter">A</div><div class="faq-q">Why partner with HFB?<svg width="8" height="12" viewBox="0 0 8 12"><path d="M1 1l5 5-5 5" stroke="var(--black)" stroke-width="2.4" fill="none"/></svg></div></div>
    <div class="faq-item"><div class="faq-letter">B</div><div class="faq-q">Who Do We Partner With?<svg width="8" height="12" viewBox="0 0 8 12"><path d="M1 1l5 5-5 5" stroke="var(--black)" stroke-width="2.4" fill="none"/></svg></div></div>
    <div class="faq-item"><div class="faq-letter">C</div><div class="faq-q">How do my network partner with HFB?<svg width="8" height="12" viewBox="0 0 8 12"><path d="M1 1l5 5-5 5" stroke="var(--black)" stroke-width="2.4" fill="none"/></svg></div></div>
    <div class="faq-item" style="min-height:76px"><div class="faq-letter">D</div><div class="faq-q">Why does HFB work with so many<br>different planting arms?<svg width="8" height="12" viewBox="0 0 8 12"><path d="M1 1l5 5-5 5" stroke="var(--black)" stroke-width="2.4" fill="none"/></svg></div></div>
  </div>
  <div class="faq-col right">
    <div class="faq-item open" style="min-height:139px"><div class="faq-letter">E</div><div class="faq-q"><div class="faq-title">Do HFB only work with minority church planters?</div><div class="faq-answer">No...while minority church planters are a demographic of planters we specialize in we also work with planters from all backgrounds</div><svg width="12" height="8" viewBox="0 0 12 8"><path d="M1 1l5 5 5-5" stroke="var(--orange)" stroke-width="2.4" fill="none"/></svg></div></div>
    <div class="faq-item"><div class="faq-letter">F</div><div class="faq-q">I want to plant a church, what do I do?<svg width="8" height="12" viewBox="0 0 8 12"><path d="M1 1l5 5-5 5" stroke="var(--black)" stroke-width="2.4" fill="none"/></svg></div></div>
    <div class="faq-item"><div class="faq-letter">G</div><div class="faq-q">In what ways can I support HFB?<svg width="8" height="12" viewBox="0 0 8 12"><path d="M1 1l5 5-5 5" stroke="var(--black)" stroke-width="2.4" fill="none"/></svg></div></div>
  </div>
</section>

<footer class="site-footer">
  <nav class="foot-nav"><a href="#">Home</a><a href="#">About Us</a><a href="#">Donate</a><a href="#">Contact Us</a><a href="#">Partners</a></nav>
  <p class="copyright">Copyright © 2021 CompanyName All Rights Reserved.</p>
  <div class="social" aria-label="Social links"><span></span><span></span><span></span><span></span><span></span></div>
</footer>
</body>
</html>
```